Business Card Design

Contact Information for Business Card

A vertical business card request- a medium & light gray with silverfern tree logo (logo is attached)

Please use Trebuchet font -- if possible- can we use two different color gray? (See pictures attached below)
Info on the front should be the Silverfern tree logo - on the top of the card, followed by the info ...
Card to read: " " indicated what should be on the card --
Name: " Joan Pelley "
Title : "Partner "
" Office: 202.555.0147 "
" Mobile: 202.555.0182 "

Backside of the card - solid medium color gray color w/ address and small message centered in the card - Trebuchet font
to read:

" 317 B North Linden Avenue, NE "
" Washington, DC 20099 "

Then below address to read:
" Fundraising | Event Planning | Political Consulting "

```html
<!DOCTYPE html>
<html lang="en">
<head>
<meta charset="utf-8">
<title>Silver Fern Strategies — Business Card</title>
<link rel="stylesheet" href="https://fonts.googleapis.com/css2?family=Open+Sans:wght@400;600&display=swap">
<style>
  :root {
    --page-bg: #e9e7e3;
    --card-dark: #6b6b6b;
    --card-light: #8e8e8e;
    --name-grey: #a9a9a9;
    --text-white: #f4f4f4;
    --logo-grey: #bdbdbd;
    --art-light: rgba(245, 245, 245, 0.55);
    --art-fade: rgba(245, 245, 245, 0);
    --shadow: rgba(0, 0, 0, 0.25);
  }
  * { box-sizing: border-box; margin: 0; padding: 0; }
  html, body {
    width: 1200px;
    height: 950px;
    overflow: hidden;
    background: var(--page-bg);
    font-family: "Open Sans", "Trebuchet MS", sans-serif;
  }
  .card-set {
    position: absolute;
    top: 90px;
    left: 120px;
    display: flex;
    gap: 80px;
  }
  .card {
    width: 440px;
    height: 770px;
    position: relative;
    overflow: hidden;
    box-shadow: 0 10px 28px var(--shadow);
    text-align: center;
  }
  .card--front { background: var(--card-dark); }
  .card--back { background: var(--card-light); }

  .contact {
    position: absolute;
    top: 80px;
    left: 0;
    right: 0;
    color: var(--text-white);
    font-size: 21px;
    line-height: 1.45;
  }
  .contact__name {
    color: var(--name-grey);
    font-size: 30px;
    font-weight: 600;
    letter-spacing: 0.5px;
  }
  .contact__title {
    font-size: 19px;
    margin-bottom: 12px;
  }

  .tree-art {
    position: absolute;
    border-radius: 50% 50% 8px 8px / 45% 45% 8px 8px;
    background: radial-gradient(ellipse at 50% 40%, var(--art-light), var(--art-fade) 72%);
  }
  .tree-art--large {
    top: 330px;
    left: 40px;
    width: 320px;
    height: 440px;
  }
  .tree-art--small {
    top: 80px;
    left: 140px;
    width: 190px;
    height: 150px;
  }

  .brand {
    position: absolute;
    top: 240px;
    left: 0;
    right: 0;
    color: var(--logo-grey);
  }
  .brand__name {
    font-size: 44px;
    font-weight: 400;
    letter-spacing: 3px;
    line-height: 1;
  }
  .brand__tag {
    font-size: 18px;
    font-weight: 400;
    letter-spacing: 3px;
    margin-top: 6px;
    padding-left: 150px;
  }

  .address {
    position: absolute;
    top: 540px;
    left: 0;
    right: 0;
    color: var(--text-white);
    font-size: 20px;
    line-height: 1.4;
  }
  .services {
    position: absolute;
    top: 630px;
    left: 0;
    right: 0;
    color: var(--text-white);
    font-size: 20px;
    line-height: 1.4;
  }
</style>
</head>
<body>
  <main class="card-set">
    <section class="card card--front">
      <div class="contact">
        <p class="contact__name">Joan Pelley</p>
        <p class="contact__title">Partner</p>
        <p class="contact__line">Office: 202.555.0147</p>
        <p class="contact__line">Mobile: 202.555.0182</p>
        <p class="contact__line">joan@silverfernllc.com</p>
      </div>
      <div class="tree-art tree-art--large" role="img" aria-label="Large white bare-branched tree illustration"></div>
    </section>

    <section class="card card--back">
      <div class="tree-art tree-art--small" role="img" aria-label="Small pale tree illustration above the company name"></div>
      <div class="brand">
        <p class="brand__name">SILVER FERN</p>
        <p class="brand__tag">STRATEGIES</p>
      </div>
      <div class="address">
        <p>317 B North Linden Avenue, NE</p>
        <p>Washington, DC 20099</p>
      </div>
      <div class="services">
        <p>Fundraising | Event Planning</p>
        <p>Political Consulting</p>
      </div>
    </section>
  </main>
</body>
</html>
```